IT Company based on Biology Business Needs a Business Card Design

We need a business card design for a new company called 'Lumen CELL'. We develop the machine learning solutions especially focused on deep learning algorithms for biology industry. Our initial product is a vision detection on biological images to help doctors diagnose the symptoms. We would like to see designs that use the color green.

Industry/Entity Type

Business

```html
<!DOCTYPE html>
<html lang="en">
<head>
<meta charset="UTF-8">
<title>Lumen CELL Business Card</title>
<link href="https://fonts.googleapis.com/css2?family=Lato:wght@400;700&display=swap" rel="stylesheet">
<style>
  :root {
    --page-bg: #ececec;
    --card-white: #ffffff;
    --green: #6ab633;
    --green-light: #7cc043;
    --green-deep: #5aa82a;
    --green-dark: #0f7a3b;
    --ink: #2e2e2e;
    --rule: #9a9a9a;
  }
  * { margin: 0; padding: 0; box-sizing: border-box; }
  html, body {
    width: 1200px; height: 750px; overflow: hidden;
    background: var(--page-bg);
    font-family: "Lato", Arial, sans-serif;
  }
  .canvas { position: relative; width: 1200px; height: 750px; }
  .card {
    position: absolute; top: 218px;
    width: 492px; height: 281px; overflow: hidden;
  }
  .card-front { left: 91px; background: var(--card-white); }
  .card-back {
    left: 620px;
    background: linear-gradient(135deg, var(--green-light), var(--green-deep));
  }

  .brand {
    position: absolute; display: flex; align-items: center;
    font-weight: 400; line-height: 1; letter-spacing: -0.5px;
  }
  .brand-dot { border-radius: 50%; flex: none; }
  .front-brand { left: 40px; top: 127px; font-size: 25px; color: var(--green); }
  .front-brand .brand-dot { width: 18px; height: 18px; background: var(--green); margin-right: 10px; }
  .back-brand {
    left: 0; right: 0; top: 122px; justify-content: center;
    font-size: 38px; color: #fff;
  }
  .back-brand .brand-dot { width: 28px; height: 28px; background: #fff; margin-right: 14px; }

  .divider {
    position: absolute; left: 247px; top: 79px;
    width: 1px; height: 134px; background: var(--rule);
  }
  .contact { position: absolute; left: 261px; top: 78px; color: var(--ink); }
  .person-name { font-size: 18px; font-weight: 700; color: var(--green); line-height: 20px; }
  .person-role { font-size: 16px; font-weight: 700; line-height: 20px; }
  .address { margin-top: 10px; font-size: 14px; line-height: 17px; }
  .contact-list { margin-top: 12px; list-style: none; font-size: 14px; line-height: 18px; }
  .contact-list li { display: flex; align-items: center; }
  .contact-list svg { width: 13px; height: 13px; margin-right: 6px; flex: none; }

  .footer-band {
    position: absolute; left: 0; bottom: 0; width: 100%; height: 19px;
    background: linear-gradient(90deg, var(--green-deep), var(--green-light));
  }
  .web-tag {
    position: absolute; left: 326px; top: 0; width: 140px; height: 19px;
    background: var(--green-dark); color: #fff;
    font-size: 13px; line-height: 19px; text-align: center;
  }
</style>
</head>
<body>
<main class="canvas">
  <section class="card card-front">
    <div class="brand front-brand"><span class="brand-dot"></span>LUMEN CELL</div>
    <div class="divider"></div>
    <div class="contact">
      <p class="person-name">Marcus Hale</p>
      <p class="person-role">Co- Founder</p>
      <p class="address">Po Box 17<br>Business address here</p>
      <ul class="contact-list">
        <li>
          <svg viewBox="0 0 16 16" aria-hidden="true"><path fill="#6ab633" d="M2 6c0-2 2-3 6-3s6 1 6 3l-2 1-1-2H5L4 7 2 6zm2 2h8l1 5H3l1-5zm4 1.5a1.5 1.5 0 1 0 0 3 1.5 1.5 0 0 0 0-3z"/></svg>
          +0147836291
        </li>
        <li>
          <svg viewBox="0 0 16 16" aria-hidden="true"><rect x="1" y="3" width="14" height="10" fill="#6ab633"/><path d="M1 3l7 6 7-6" fill="none" stroke="#fff" stroke-width="1.3"/></svg>
          info@lumencell.com
        </li>
      </ul>
    </div>
    <div class="footer-band"><span class="web-tag">www.lumencell.com</span></div>
  </section>

  <section class="card card-back">
    <div class="brand back-brand"><span class="brand-dot"></span>LUMEN CELL</div>
  </section>
</main>
</body>
</html>
```